Stationary design for a bidet toilet seat
Vellora Bidets
Stationary design for a bidet toilet seat  - Health
Creative Brief
Bright & Fun-filled
Tobias Merrick III
Marketing Agent
418 Westmere Ave. Suite 203 Houston, TX 77024
vellorabidets@quillpost-mail.com
My logo was done by Quorvan designs

```html
<!DOCTYPE html>
<html lang="en">
<head>
<meta charset="utf-8">
<title>Vellora Bidets — Business Cards</title>
<link rel="stylesheet" href="https://fonts.googleapis.com/css2?family=Cinzel:wght@400;600&family=Lato:wght@400&display=swap">
<style>
  :root{
    --stage:#8c8e90;
    --blue:#2f86d6;
    --blue-deep:#1f6fc0;
    --blue-light:#4ea0e6;
    --green:#5aa83a;
    --ink:#3a3f45;
    --paper:#ffffff;
    --faint:rgba(200,215,255,.55);
  }
  *{box-sizing:border-box;margin:0;padding:0}
  html,body{width:1200px;height:908px;overflow:hidden}
  body{background:var(--stage);position:relative;font-family:"Lato",sans-serif}

  .card{position:absolute;top:306px;width:520px;height:297px;border-radius:22px;overflow:hidden;
        box-shadow:0 10px 24px rgba(0,0,0,.25)}
  .card--front{left:50px;background:linear-gradient(135deg,var(--blue-light),var(--blue-deep))}
  .card--back{left:630px;background:var(--paper)}

  .front__ring{position:absolute;left:-70px;top:70px;width:300px;height:300px;border-radius:50%;
               border:5px solid var(--faint);background:rgba(150,200,190,.35)}
  .front__name{position:absolute;right:38px;top:118px;font-family:"Cinzel",serif;font-weight:600;
               font-size:30px;color:var(--paper);letter-spacing:1px}

  .back__band{position:absolute;left:0;right:0;height:30px;background:var(--blue)}
  .back__band--top{top:0}
  .back__band--bottom{bottom:0}
  .back__rule{position:absolute;left:0;right:0;height:2px;background:var(--green)}
  .back__rule--top{top:38px}
  .back__rule--bottom{bottom:38px}

  .back__logo{position:absolute;left:34px;top:168px;display:flex;align-items:center;gap:10px}
  .back__logo-dot{width:34px;height:34px;border-radius:50%;background:var(--blue)}
  .back__logo-name{font-family:"Cinzel",serif;font-weight:600;font-size:22px;color:var(--blue-deep)}

  .back__contact{position:absolute;left:262px;top:64px}
  .back__person{font-family:"Cinzel",serif;font-weight:600;font-size:19px;color:var(--green);letter-spacing:.5px}
  .back__role{font-family:"Cinzel",serif;font-size:12px;color:var(--green);letter-spacing:1px;margin-top:2px}
  .back__divider{width:220px;height:1px;background:var(--green);margin:12px 0}
  .back__line{font-size:11.5px;color:var(--ink);line-height:1.6;display:flex;align-items:center;gap:6px}
  .back__line svg{width:11px;height:11px;flex:none}
</style>
</head>
<body>
  <section class="card card--front" aria-label="Card front">
    <div class="front__ring"></div>
    <div class="front__name">Vellora Bidets</div>
  </section>

  <section class="card card--back" aria-label="Card back">
    <div class="back__band back__band--top"></div>
    <div class="back__rule back__rule--top"></div>

    <div class="back__logo">
      <span class="back__logo-dot"></span>
      <span class="back__logo-name">Vellora Bidets</span>
    </div>

    <div class="back__contact">
      <div class="back__person">TOBIAS MERRICK III</div>
      <div class="back__role">MARKETING AGENT</div>
      <div class="back__divider"></div>
      <div class="back__line">418 Westmere Ave.</div>
      <div class="back__line">Suite 203, Houston, TX 77024</div>
      <div class="back__line">
        <svg viewBox="0 0 12 12"><circle cx="6" cy="6" r="6" fill="#5aa83a"/><path d="M4 3.2l1 1.6-.6.6c.4.9 1 1.5 1.9 1.9l.6-.6 1.6 1-.5 1.2C5.6 8.8 3.2 6.4 3 3.7z" fill="#fff"/></svg>
        713-555-0142
      </div>
      <div class="back__line">
        <svg viewBox="0 0 12 12"><circle cx="6" cy="6" r="6" fill="#5aa83a"/><path d="M4 3.2l1 1.6-.6.6c.4.9 1 1.5 1.9 1.9l.6-.6 1.6 1-.5 1.2C5.6 8.8 3.2 6.4 3 3.7z" fill="#fff"/></svg>
        713-555-0187
      </div>
      <div class="back__line">
        <svg viewBox="0 0 12 12"><circle cx="6" cy="6" r="6" fill="#5aa83a"/><rect x="3" y="4" width="6" height="4.2" fill="none" stroke="#fff" stroke-width=".9"/><path d="M3 4l3 2.4L9 4" fill="none" stroke="#fff" stroke-width=".9"/></svg>
        vellorabidets@quillpost-mail.com
      </div>
    </div>

    <div class="back__rule back__rule--bottom"></div>
    <div class="back__band back__band--bottom"></div>
  </section>
</body>
</html>
```